Lifestyle Coaching comp needs wordpress design. We focus on strong mindsets, fitness and nutrition

BrimOak Lifestyle Coaching needs a wordpress site. Our tagline for now (may change) is Mindset Mastery.Fitness Badassery. Sustainable Nutrition
Our logo is below. Would like to see some complimentary colors to liven it up. Clients need to come to site and get immediate professional, but fun feel. They need to have the impression that we are the last destination in their journey to wellness. Blogging, workout videos, pictures

Target Market(s)

Mostly women ages 20+

Industry/Entity Type

Nutrition

Colors
33a6d7
86cae7
ceeaf6
cfdeed
5c5c5c
cbcbcb
474747

Requirements
Must have
• A strong, badass feel :) While not being intimidating
Nice to have
• Fun fonts. Love the font in my logo
Should not have
• Pics, logos of flowers, heads, fruit.

```html
<!DOCTYPE html>
<html lang="en">
<head>
<meta charset="utf-8">
<title>BrimOak Lifestyle Coaching</title>
<link href="https://fonts.googleapis.com/css2?family=Oswald:wght@400;500&family=Roboto:wght@400;500&display=swap" rel="stylesheet">
<style>
:root{
  --blue:#33a6d7;
  --blue-mid:#86cae7;
  --blue-dark:#1d5f98;
  --ink:#2b2b2b;
  --band:#221f1d;
  --muted:#b9b9b9;
  --white:#ffffff;
}
*{margin:0;padding:0;box-sizing:border-box}
html,body{width:734px;height:1200px;overflow:hidden;background:#000}
body{position:relative;font-family:"Roboto",Arial,sans-serif}
.abs{position:absolute}
.header{left:0;top:0;width:734px;height:78px;background:linear-gradient(#fff,#ececec)}
.brand{left:55px;top:26px;display:flex;align-items:center;gap:8px}
.brand-dot{width:20px;height:20px;border-radius:50%;background:var(--blue)}
.brand-name{font-family:"Oswald",sans-serif;font-weight:500;font-size:22px;line-height:1;color:var(--blue-dark);letter-spacing:2px}
.nav{left:324px;top:30px;font-family:"Oswald",sans-serif;font-size:12.5px;color:var(--ink)}
.nav a{position:absolute;white-space:nowrap;text-decoration:none;color:inherit}
.nav a.active{color:var(--blue)}
.hero{left:0;top:78px;width:734px;height:413px;background:
  radial-gradient(ellipse 90px 140px at 490px 300px,rgba(110,200,210,.85),transparent 70%),
  radial-gradient(ellipse 110px 170px at 380px 200px,rgba(80,100,140,.9),transparent 70%),
  radial-gradient(ellipse 70px 90px at 190px 300px,rgba(240,120,170,.7),transparent 70%),
  radial-gradient(ellipse 60px 110px at 60px 300px,rgba(40,90,220,.8),transparent 70%),
  radial-gradient(ellipse 60px 70px at 488px 250px,rgba(236,60,190,.9),transparent 70%),
  radial-gradient(ellipse 80px 90px at 370px 90px,rgba(210,150,120,.7),transparent 70%),
  radial-gradient(ellipse 80px 90px at 560px 140px,rgba(200,140,110,.7),transparent 70%),
  linear-gradient(180deg,#4f9cc8 0%,#7fb6d6 30%,#3b5a7a 75%,#1d2a3a 100%)}
.tagline{left:64px;top:210px;width:293px;height:130px;background:rgba(35,35,40,.5)}
.tagline p{position:absolute;left:14px;font-family:"Oswald",sans-serif;font-weight:500;font-size:27px;line-height:1;color:var(--white);white-space:nowrap;letter-spacing:-.3px;text-shadow:0 2px 3px rgba(0,0,0,.45)}
.tagline .accent{color:var(--blue-mid)}
.band{left:0;top:491px;width:734px;height:129px;background:var(--band);border-bottom:3px solid var(--blue-dark)}
.features{left:0;top:623px;width:734px;height:287px;background:linear-gradient(#262626,#000)}
.card{width:200px}
.card .thumb{position:relative;width:200px;height:118px;border:2px solid #eee}
.card h3{margin-top:22px;font-family:"Oswald",sans-serif;font-weight:400;font-size:14.5px;line-height:1;color:var(--blue-mid);padding-left:4px}
.card p{margin-top:9px;width:178px;font-size:8.2px;line-height:11.8px;color:var(--muted);text-align:justify}
.btn{display:inline-block;margin-top:8px;width:64px;height:22px;line-height:22px;text-align:center;background:linear-gradient(#2a76b8,#1b528a);color:#fff;font-size:8.5px;border-radius:2px}
.blogs{left:0;top:910px;width:734px;height:198px;background:
  radial-gradient(ellipse 120px 90px at 250px 140px,rgba(20,20,20,.6),transparent 70%),
  radial-gradient(ellipse 140px 120px at 560px 60px,rgba(170,140,120,.45),transparent 70%),
  linear-gradient(90deg,#3a4650,#56636a 50%,#3b4a55)}
.blogs h2{position:absolute;left:0;width:734px;top:14px;text-align:center;font-family:"Oswald",sans-serif;font-weight:400;font-size:19px;color:var(--blue-mid)}
.post{display:flex;gap:14px}
.post .pthumb{flex:none;width:99px;height:85px;border:2px solid #eee;border-radius:3px}
.post h4{font-weight:400;font-size:10px;line-height:1;color:var(--blue-mid);letter-spacing:.3px;margin-top:2px}
.post p{margin-top:5px;font-size:7.6px;line-height:13.6px;color:#f2f2f2;width:188px}
.post .more{margin-top:2px;font-size:7.6px;color:var(--blue-mid)}
.footer{left:0;top:1108px;width:734px;height:92px;background:#000}
.social{width:20px;height:20px;border-radius:2px}
.legal{right:56px;top:1134px;text-align:right;font-size:8.5px;line-height:18px;color:#ddd}
</style>
</head>
<body>
<header class="abs header">
  <div class="abs brand"><span class="brand-dot"></span><span class="brand-name">BrimOak</span></div>
  <nav class="abs nav">
    <a class="active" style="left:0">HOME</a>
    <a style="left:46px">ABOUT US</a>
    <a style="left:111px">FITNESS</a>
    <a style="left:165px">COACHING</a>
    <a style="left:231px">NEWS</a>
    <a style="left:280px">CONTACTS</a>
  </nav>
  <svg class="abs" style="left:663px;top:31px" width="14" height="14" viewBox="0 0 14 14"><circle cx="5.5" cy="5.5" r="4" fill="none" stroke="#33a6d7" stroke-width="2"/><line x1="8.5" y1="8.5" x2="12.5" y2="12.5" stroke="#33a6d7" stroke-width="2.4"/></svg>
</header>

<section class="abs hero" role="img" aria-label="Smiling couple training with dumbbells in a bright gym, group of athletes behind them"></section>
<div class="abs tagline">
  <p style="top:18px">MINDSET MASTERY.</p>
  <p class="accent" style="top:54px">FITNESS BADASSERY.</p>
  <p style="top:90px">SUSTAINABLE NUTRITION.</p>
</div>
<svg class="abs" style="left:28px;top:255px" width="678" height="46" viewBox="0 0 678 46">
  <polyline points="22,2 4,23 22,44" fill="none" stroke="#fff" stroke-width="1.5"/>
  <polyline points="656,2 674,23 656,44" fill="none" stroke="#fff" stroke-width="1.5"/>
</svg>

<section class="abs band"></section>
<svg class="abs" style="left:0;top:385px" width="734" height="220" viewBox="0 0 734 220">
  <path d="M55 106 A104 109 0 0 0 263 106 Z" fill="#000" stroke="#33a6d7" stroke-width="2"/>
  <path d="M57 106 A102 81 0 0 0 261 106 Z" fill="#221f1d" stroke="#33a6d7" stroke-width="2"/>
  <path d="M471 106 A104 109 0 0 0 679 106 Z" fill="#000" stroke="#33a6d7" stroke-width="2"/>
  <path d="M473 106 A102 81 0 0 0 677 106 Z" fill="#221f1d" stroke="#33a6d7" stroke-width="2"/>
  <rect x="0" y="104" width="734" height="3" fill="#221f1d"/>
  <circle cx="366" cy="109" r="105" fill="#000" stroke="#33a6d7" stroke-width="3"/>
  <g fill="#bfe4f5">
    <rect x="338" y="66" width="9" height="26" rx="2"/><rect x="385" y="66" width="9" height="26" rx="2"/>
    <rect x="347" y="75" width="38" height="8"/>
    <rect x="324" y="71" width="11" height="16" rx="2"/><rect x="397" y="71" width="11" height="16" rx="2"/>
    <rect x="352" y="94" width="28" height="10" rx="3"/>
  </g>
  <polyline points="287,104 282,109 287,114" fill="none" stroke="#fff" stroke-width="1.5"/>
  <polyline points="443,104 448,109 443,114" fill="none" stroke="#fff" stroke-width="1.5"/>
  <text x="366" y="156" text-anchor="middle" font-family="Oswald,sans-serif" font-size="17" fill="#fff">Lifestyle Coaching</text>
  <circle cx="143" cy="140" r="7" fill="#33a6d7"/>
  <polyline points="139.5,140 142,143 146.5,137" fill="none" stroke="#000" stroke-width="1.8"/>
  <text x="157" y="147" font-family="Oswald,sans-serif" font-size="17" fill="#fff">TIP</text>
  <polyline points="155,166 159,170 163,166" fill="none" stroke="#fff" stroke-width="1.3"/>
  <polyline points="155,171 159,175 163,171" fill="none" stroke="#fff" stroke-width="1.3"/>
  <rect x="541" y="134" width="18" height="13" fill="none" stroke="#33a6d7" stroke-width="1.5"/>
  <rect x="545" y="138" width="5" height="5" fill="#33a6d7"/>
  <line x1="552" y1="139" x2="556" y2="139" stroke="#33a6d7"/><line x1="552" y1="142" x2="556" y2="142" stroke="#33a6d7"/>
  <text x="571" y="147" font-family="Oswald,sans-serif" font-size="17" fill="#fff">NEWS</text>
  <polyline points="571,166 575,170 579,166" fill="none" stroke="#fff" stroke-width="1.3"/>
  <polyline points="571,171 575,175 579,171" fill="none" stroke="#fff" stroke-width="1.3"/>
</svg>

<section class="abs features">
  <article class="abs card" style="left:54px;top:33px">
    <div class="thumb" role="img" aria-label="Group aerobics class in bright gym clothes" style="background:
      radial-gradient(ellipse 26px 40px at 45px 60px,rgba(120,190,230,.9),transparent 70%),
      radial-gradient(ellipse 26px 40px at 100px 60px,rgba(250,250,250,.9),transparent 70%),
      radial-gradient(ellipse 26px 40px at 155px 60px,rgba(255,255,255,.95),transparent 70%),
      linear-gradient(180deg,#e9edf1 0%,#cfd6dd 55%,#1e1e22 78%,#b8bec4 100%)"></div>
    <h3>FITNESS AND NUTRITION</h3>
    <p>Lorem Ipsum has been the industry's standard dummy text ever since the 1500s, when an unknown printer took a galley of type</p>
    <span class="btn">Read More</span>
  </article>
  <article class="abs card" style="left:267px;top:33px">
    <div class="thumb" role="img" aria-label="Woman running on a treadmill in a gym" style="background:
      radial-gradient(ellipse 22px 36px at 75px 62px,rgba(30,160,210,.95),transparent 70%),
      radial-gradient(ellipse 50px 60px at 150px 80px,rgba(120,120,125,.8),transparent 70%),
      linear-gradient(180deg,#f2f2f2 0%,#d9dbdd 50%,#6b6e72 100%)"></div>
    <h3>PICTURES</h3>
    <p>Lorem Ipsum has been the industry's standard dummy text ever since the 1500s, when an unknown printer took a galley of type</p>
    <span class="btn">View More</span>
  </article>
  <article class="abs card" style="left:480px;top:33px">
    <div class="thumb" role="img" aria-label="Workout video of a class doing sit-ups on mats" style="background:
      radial-gradient(ellipse 40px 18px at 40px 78px,rgba(190,230,60,.95),transparent 70%),
      radial-gradient(ellipse 30px 16px at 150px 78px,rgba(240,110,150,.9),transparent 70%),
      linear-gradient(180deg,#3b3f3c 0%,#8a8a82 35%,#c98a4e 65%,#2f6fb0 88%,#1a1a1a 100%)">
      <svg class="abs" style="left:80px;top:39px" width="32" height="32" viewBox="0 0 32 32"><circle cx="16" cy="16" r="15" fill="rgba(0,0,0,.6)"/><polygon points="12,9 24,16 12,23" fill="#fff"/></svg>
    </div>
    <h3>WORKOUT VIDEOS</h3>
    <p>Lorem Ipsum has been the industry's standard dummy text ever since the 1500s, when an unknown printer took a galley of type</p>
    <span class="btn">View More</span>
  </article>
</section>

<section class="abs blogs" role="img" aria-label="Faded background of a woman lifting a dumbbell">
  <h2>LATEST BLOGS</h2>
  <article class="abs post" style="left:56px;top:68px">
    <div class="pthumb" role="img" aria-label="Women training with resistance bands" style="background:
      radial-gradient(ellipse 30px 26px at 30px 70px,rgba(240,120,30,.95),transparent 70%),
      radial-gradient(ellipse 26px 26px at 70px 72px,rgba(60,80,190,.9),transparent 70%),
      linear-gradient(180deg,#f4f1ec,#e6c9b0 55%,#e07a3a)"></div>
    <div><h4>IPSUM IS SIMPLY DUMMY TEXT</h4><p>Lorem Ipsum is simply dummy text of the printing and typesetting industry. Lorem Ipsum has been the indus-try's standard dummy text ever since the 1500s, when</p><div class="more">VIEW MORE &gt;&gt;</div></div>
  </article>
  <article class="abs post" style="left:381px;top:67px">
    <div class="pthumb" role="img" aria-label="Man lifting a barbell in the gym" style="background:
      radial-gradient(ellipse 16px 26px at 52px 52px,rgba(210,30,40,.95),transparent 70%),
      radial-gradient(circle 14px at 18px 36px,rgba(20,20,20,.95),transparent 80%),
      radial-gradient(circle 12px at 80px 36px,rgba(30,30,30,.9),transparent 80%),
      linear-gradient(180deg,#f0f0f0,#c9cbcd 60%,#8a8d90)"></div>
    <div><h4>IPSUM IS SIMPLY DUMMY TEXT</h4><p>Lorem Ipsum is simply dummy text of the printing and typesetting industry. Lorem Ipsum has been the indus-try's standard dummy text ever since the 1500s, when</p><div class="more">VIEW MORE &gt;&gt;</div></div>
  </article>
</section>

<footer class="abs footer">
  <div class="abs brand" style="left:60px;top:36px"><span class="brand-dot"></span><span class="brand-name" style="color:#fff">BrimOak</span></div>
  <span class="abs social" aria-label="Social link" style="left:318px;top:32px;background:#2a8fd0"></span>
  <span class="abs social" aria-label="Social link" style="left:346px;top:32px;background:#c4302b"></span>
  <span class="abs social" aria-label="Social link" style="left:372px;top:32px;background:#3b5998"></span>
  <span class="abs social" aria-label="Social link" style="left:398px;top:32px;background:#1b6bb0"></span>
</footer>
<div class="abs legal">Privacy Policy &nbsp;|&nbsp; Terms of Use<br>Copyright © 2015 &nbsp;All Rights</div>
</body>
</html>
```